Flyer: helping to close the Global Digital Divide- R22 project.

We need a flyer designing for a nonprofit (www.plumvorta.org) based in Washington DC and London. We help to connect communities that have no internet so that they can get access to the health, educational, socio-economic benefits of internet connectivity. The project is ‘R22’ – internet for the Blue Tide.
The flyer will be sent to major corporations, governments, major universities, and the like.
The first half of the flyer will be design rich and incorporate the words (on the attached R22 document) in a creative and appealing way using design and color contrasts to highlight important points. The R22 Logo is attached also. I have also attached a similar but different KOVL document to give some ideas.
The second half of the flyer will be an MOU (Memorandum of Understanding) for the corporations to sign. This needs to be simple and look professional.
It is very important that we can change the words in the flyer once the design is complete without having to go back to the designer every time.

```html
<!DOCTYPE html>
<html lang="en">
<head>
<meta charset="utf-8">
<title>R22 Charter MOU – Terms</title>
<link rel="stylesheet" href="https://fonts.googleapis.com/css2?family=Montserrat:wght@400;600;700&display=swap">
<style>
  :root {
    --ink: #1c1c24;
    --paper: #ffffff;
    --mesh: #33e6c8;
    --band-start: #15306a;
    --band-end: #1b0b2a;
    --band-text: #ffffff;
  }
  html, body {
    margin: 0;
    padding: 0;
    overflow: hidden;
    background: var(--paper);
  }
  .page {
    position: relative;
    width: 848px;
    height: 1200px;
    overflow: hidden;
    background: var(--paper);
    font-family: "Montserrat", sans-serif;
    color: var(--ink);
  }
  .mesh {
    position: absolute;
    display: block;
  }
  .mesh--top { top: 0; right: 0; width: 300px; height: 330px; }
  .mesh--side { top: 610px; right: 0; width: 130px; height: 470px; }
  .mesh--bottom { bottom: 0; left: 200px; width: 648px; height: 190px; }

  .terms {
    position: absolute;
    top: 68px;
    left: 57px;
    width: 795px;
    font-size: 15.1px;
    line-height: 18.8px;
  }
  .clause {
    margin: 0 0 18.8px;
  }
  .clause__title {
    font-weight: 600;
  }

  .cta-band {
    position: absolute;
    top: 875px;
    left: 0;
    width: 786px;
    height: 153px;
    background: linear-gradient(90deg, var(--band-start), var(--band-end));
    color: var(--band-text);
    font-weight: 600;
    font-size: 16.4px;
    line-height: 22px;
    box-sizing: border-box;
    padding: 30px 0 0 58px;
  }
  .cta-band p { margin: 0; }
  .cta-band .cta-return { margin-bottom: 21px; }
</style>
</head>
<body>
<div class="page">

  <svg class="mesh mesh--top" viewBox="0 0 300 330" role="img" aria-label="Decorative connected-network pattern in teal" preserveAspectRatio="none">
    <defs>
      <radialGradient id="meshTop" cx="1" cy="0" r="1">
        <stop offset="0" stop-color="#33e6c8" stop-opacity="0.35"/>
        <stop offset="1" stop-color="#33e6c8" stop-opacity="0"/>
      </radialGradient>
    </defs>
    <rect width="300" height="330" fill="url(#meshTop)"/>
  </svg>

  <svg class="mesh mesh--side" viewBox="0 0 130 470" role="img" aria-label="Decorative connected-network pattern in teal" preserveAspectRatio="none">
    <defs>
      <linearGradient id="meshSide" x1="1" y1="0.5" x2="0" y2="0.5">
        <stop offset="0" stop-color="#33e6c8" stop-opacity="0.3"/>
        <stop offset="1" stop-color="#33e6c8" stop-opacity="0"/>
      </linearGradient>
    </defs>
    <rect width="130" height="470" fill="url(#meshSide)"/>
  </svg>

  <svg class="mesh mesh--bottom" viewBox="0 0 648 190" role="img" aria-label="Decorative connected-network pattern in teal" preserveAspectRatio="none">
    <defs>
      <linearGradient id="meshBottom" x1="0.5" y1="1" x2="0.5" y2="0">
        <stop offset="0" stop-color="#33e6c8" stop-opacity="0.32"/>
        <stop offset="1" stop-color="#33e6c8" stop-opacity="0"/>
      </linearGradient>
    </defs>
    <rect width="648" height="190" fill="url(#meshBottom)"/>
  </svg>

  <section class="terms">
    <p class="clause"><span class="clause__title">4. Confidentiality and Public Announcement:</span> Each Party must treat the other party’s Confidential Information (as defined in the CNDA) in accordance with the CNDA identified on the first page of this MOU. The CNDA is a separate agreement and will survive the expiration or termination of this MOU. Neither Party will make any public announcement about the MOU (or the subject matter of this MOU), without the prior written consent of the other Party.</p>

    <p class="clause"><span class="clause__title">5. License:</span> No license is granted under this MOU to either Party under any of the other Party’s intellectual property rights.</p>

    <p class="clause"><span class="clause__title">6. Nature of relationship:</span> The Parties are independent contractors, and no agency, partnership, franchise or joint venture is intended or created by this MOU. This MOU does not create an exclusive relationship between the Parties regarding the subject matter of this MOU.</p>

    <p class="clause"><span class="clause__title">7. Entire Understanding:</span> This MOU constitutes the entire understanding between the Parties regarding its subject matter. Neither Party has relied on any statements or representations made by the other in connection with this MOU, which are not set out in this MOU.</p>

    <p class="clause"><span class="clause__title">8. Exclusion of Liability:</span> Neither Party will have any liability whatsoever to the other Party under or in connection with this MOU or any Engagement, either in contract, tort or otherwise (including, without limitation, for negligence and misrepresentation), for: (a) loss of revenue; (b) loss of actual or anticipated profits; (c) loss of anticipated savings; (d) loss of reputation; (e) loss of, damage to or corruption of data; or (f) any indirect or consequential loss or damage howsoever arising. This exclusion of liability clause will not apply to any liability arising from breach of the obligations set out in Section 4 of this MOU.</p>

    <p class="clause"><span class="clause__title">9. Governing Law &amp; Dispute Resolution:</span> All disputes arising out of or related to this MOU, whether based on contract, tort, or any other legal or equitable theory, (a) will in all respects be governed by, and construed and interpreted under, the laws of the United States of America and the State of Delaware without reference to conflict of laws principles, and (b) will be subject to the exclusive jurisdiction of the courts of the State of Delaware or of the Federal courts sitting in that State. Each party submits to the personal jurisdiction of those courts and waives all objections to that jurisdiction and venue for those disputes.</p>

    <p class="clause"><span class="clause__title">10. Language, Amendments and Severability:</span>&nbsp; This MOU will be executed in English and the English language original of this MOU will prevail over any translation of it into any other languages. No amendments to this MOU will be effective unless made in writing and signed by authorized representatives of each Party. If any provision or part of these Sections 1 to 10 is held invalid or unenforceable under applicable law, the provision or part will be modified to the minimum extent necessary to make it valid and enforceable, or if it cannot be made valid and enforceable, the provision or part will be severed from this MOU.</p>
  </section>

  <aside class="cta-band">
    <p class="cta-return">Simply sign the R22 Charter MOU above and return it to [R22@plumvorta.org]</p>
    <p class="cta-contact">To read more or to contact R22 staff, please visit [www.r22.org]<br>or write to [R22@plumvorta.org]</p>
  </aside>

</div>
</body>
</html>
```